Brevin Finance Flyer Design

I would like a high res flyer designed for mass printing. It is for a mortgage and finance broking company in Sydney. We are called Brevin Finance. The wording i would like displayed is the following
Looking For Something Extra from your broker?
Brevin Finance can make all the difference
What we offer you is an extensive range of mortgage and finance products, including:
• Home Loans
• Investment Loans
• Low Doc Loans
• Vehicle Finance
• Equipment Finance
• Commercial Loans
• Refinance
Contact Us
Phone (02) 7354 2816
email info@brevinfinance.com.au
web www.brevinfinance.com.au
Finance

```html
<!DOCTYPE html>
<html lang="en">
<head>
<meta charset="utf-8">
<title>Brevin Finance Flyer</title>
<link rel="stylesheet" href="https://fonts.googleapis.com/css2?family=Ubuntu:wght@400;500&display=swap">
<style>
  :root {
    --backdrop: #e6e6e6;
    --paper: #ffffff;
    --sand: #e9d3a4;
    --ink: #2f2f2f;
    --logo-ink: #3a3a3a;
    --body-ink: #555555;
    --footer: #1e1e1e;
    --gold: #d8bf88;
    --hero-light: #f1f5f9;
    --hero-mid: #c3cfdd;
    --hero-dark: #3a4d76;
  }
  * { margin: 0; padding: 0; box-sizing: border-box; }
  html, body { width: 1200px; height: 1200px; overflow: hidden; }
  body { background: var(--backdrop); font-family: "Ubuntu", sans-serif; color: var(--ink); }

  .flyer {
    position: absolute; left: 215px; top: 98px;
    width: 710px; height: 1004px;
    background: var(--paper); overflow: hidden;
  }

  .hero-photo {
    position: absolute; left: 0; top: 0; width: 710px; height: 487px;
    background: linear-gradient(90deg, var(--hero-light) 0%, var(--hero-light) 45%, var(--hero-mid) 68%, var(--hero-dark) 100%);
  }

  .brand { position: absolute; left: 47px; top: 52px; }
  .brand-name {
    display: flex; align-items: center; gap: 12px;
    font-size: 48px; font-weight: 400; color: var(--logo-ink); line-height: 1;
  }
  .brand-mark { width: 34px; height: 34px; background: var(--logo-ink); flex: none; }
  .brand-tagline { margin: 6px 0 0 46px; font-size: 15px; color: var(--logo-ink); }

  .headline { position: absolute; left: 34px; top: 164px; font-weight: 400; }
  .headline span {
    display: block; background: var(--sand); margin-bottom: 3px;
    font-size: 31px; font-weight: 400; line-height: 56px;
    padding: 0 24px; width: max-content;
  }

  .offer-band {
    position: absolute; left: 0; top: 487px; width: 710px; height: 278px;
    background: var(--sand); text-align: center;
  }
  .offer-title { margin-top: 33px; font-size: 24px; letter-spacing: 1.2px; font-weight: 400; }
  .offer-rule { width: 610px; height: 1px; background: var(--logo-ink); margin: 24px auto 0; border: 0; }
  .offer-intro { margin-top: 32px; font-size: 15px; letter-spacing: 2.2px; line-height: 21px; color: var(--logo-ink); }
  .product-list { margin-top: 14px; font-size: 15px; font-weight: 500; line-height: 22px; letter-spacing: 0.3px; }

  .about {
    position: absolute; left: 41px; top: 804px; width: 555px;
    font-size: 12.5px; line-height: 16px; color: var(--body-ink);
  }
  .about p { margin-bottom: 5px; }

  .contact-bar {
    position: absolute; left: 0; top: 948px; width: 710px; height: 56px;
    background: var(--footer); color: var(--gold);
    display: flex; justify-content: center; align-items: center; gap: 22px;
    font-size: 14.5px; letter-spacing: 0.4px;
  }
</style>
</head>
<body>
  <article class="flyer">
    <div class="hero-photo" role="img" aria-label="Photo area: business people in a bright office corridor"></div>

    <header class="brand">
      <div class="brand-name"><span class="brand-mark"></span>Brevin Finance</div>
      <div class="brand-tagline">mortgage and finance broking services</div>
    </header>

    <h1 class="headline">
      <span>Looking For Something</span>
      <span>Extra from your</span>
      <span>broker?</span>
    </h1>

    <section class="offer-band">
      <h2 class="offer-title">BREVIN FINANCE CAN MAKE ALL THE DIFFERENCE</h2>
      <hr class="offer-rule">
      <p class="offer-intro">WHAT WE OFFER YOU IS AN EXTENSIVE RANGE OF<br>MORTGAGE AND FINANCE PRODUCTS, INCLUDING:</p>
      <p class="product-list">
        Home Loans &nbsp;•&nbsp; Investment Loans &nbsp;•&nbsp; Low Doc Loans<br>
        Vehicle Finance &nbsp;•&nbsp; Equipment Finance &nbsp;•&nbsp; Commercial Loans<br>
        Refinance
      </p>
    </section>

    <section class="about">
      <p>Brevin Finance are brokers set up to provide clients with mortgage and finance broking services. We are based in Sydney’s North but offer our expertise to clients throughout Australia.</p>
      <p>When dealing with Brevin Finance your enquiry will be dealt with by a true finance broker expert from the outset so you will be confident that you are getting the right information and advice.</p>
      <p>With years of hands on experience we will quickly work with you to determine which lenders will approve your loan and from there work with you to decide on the best lender and loan.</p>
    </section>

    <footer class="contact-bar">
      <span>(02) 7354 2816</span><span>|</span>
      <span>info@brevinfinance.com.au</span><span>|</span>
      <span>www.brevinfinance.com.au</span>
    </footer>
  </article>
</body>
</html>
```